Outpost Lattice Advisors – Franchise Growth & Development Presentation

Outpost Lattice Advisors is an outsourced franchise sales organization (FSO) that helps franchisors grow their franchise systems without the expense and risk of hiring an internal franchise development team.

We are seeking a professional PowerPoint presentation that will be used to present our services to franchisors, franchise executives, founders, and growth-stage franchise brands.

The presentation should communicate the value of partnering with Outpost Lattice Advisors, including:

• Fractional franchise sales team versus hiring internal staff
• 30+ years of franchise industry experience
• 550+ franchise sales successes
• Immediate access to established franchise broker relationships
• Proven franchise development processes
• Franchise growth strategy and enterprise value creation
• Potential private equity and exit opportunities through franchise expansion

The presentation should feel like a modern consulting, investment, or growth strategy presentation rather than a typical sales brochure. We want strong visual storytelling, custom infographics, professional diagrams, and clean business-oriented design.

The audience includes business owners, franchise founders, franchise executives, and investors who are evaluating growth strategies for their franchise systems.

Target Market(s)

Primary Audience: Emerging franchisors Growth-stage franchise brands Franchise founders Franchise CEOs Franchise presidents Franchise development executives Secondary Audience: Private equity firms Franchise investors Strategic buyers Franchise consultants

Industry/Entity Type

Franchise Development, Private Equity / Business Expansion

Font styles to use
Other font styles liked:
• Use Montserrat for titles and Open Sans for body text.

Requirements
Must have
• Modern professional business design Consistent branding throughout Custom infographics Comparison graphics Broker network ecosystem graphic Enterprise value graphic Easy-to-read charts and visuals Editable PowerPoint format Professional iconography. www.outpostlatticeadvisors.example as reference for colors
Nice to have
• Franchise-related imagery Subtle growth-themed visuals Timeline graphics Data visualization Private equity / valuation style graphics
Should not have
• Cartoon graphics Clip art Overly busy slides Stock-template appearance Bright neon colors Handwritten fonts Excessive text on slides Juvenile or playful design elements

```html
<!DOCTYPE html>
<html lang="en">
<head>
<meta charset="utf-8">
<title>Outpost Lattice Advisors – Franchise Growth Presentation</title>
<link href="https://fonts.googleapis.com/css2?family=Montserrat:wght@500;600;700;800&family=Open+Sans:ital,wght@0,400;0,600;0,700;1,400;1,600&display=swap" rel="stylesheet">
<style>
:root{
  --navy:#13294b;
  --orange:#f29d17;
  --canvas:#e2e0e3;
  --slide:#f4f6fa;
  --card:#ffffff;
  --line:#e2e6ed;
  --muted:#6c7588;
  --ink:#1c2a3e;
  --pill:#e6e9ef;
}
*{box-sizing:border-box}
html,body{margin:0;padding:0;overflow:hidden}
body{width:891px;height:1200px;background:var(--canvas);position:relative;font-family:'Open Sans',sans-serif;color:var(--ink)}
.s{position:absolute;width:484px;height:272px;background:var(--slide);transform:scale(.5394);transform-origin:0 0;overflow:hidden}
.s *{position:absolute}
.s .flow,.s .flow *{position:static}
.s .flow .abs{position:absolute}
.eb{left:27px;top:22px;font:600 4.6px/1 'Montserrat',sans-serif;letter-spacing:.15em;color:var(--orange);text-transform:uppercase}
.t{left:27px;top:30px;margin:0;font:700 14px/1.25 'Montserrat',sans-serif;color:var(--navy)}
.t em{font-style:normal;color:var(--orange);position:static}
.rule{width:18px;height:1.5px;background:var(--orange)}
.lead{font-size:5px;line-height:1.55;color:var(--muted)}
.foot{left:27px;right:27px;bottom:14px;display:grid;grid-template-columns:1fr 1fr 1fr;font:600 4.2px 'Montserrat',sans-serif;letter-spacing:.08em;color:#8a93a3}
.foot span{position:static}
.foot span:nth-child(2){text-align:center}
.foot span:nth-child(3){text-align:right}
.card{background:var(--card);border:1px solid var(--line);border-radius:4px}
.navy{background:var(--navy);color:#fff}
.ic{width:10px;height:10px;border-radius:2px;background:var(--orange)}
.ring{width:14px;height:14px;border-radius:50%;border:1px solid #cfd5df;background:#fff;flex:none}
.ring::after{content:"";position:absolute;left:4px;top:4px;width:4px;height:4px;border-radius:1px;background:var(--navy)}
.h{font:700 5.6px/1.3 'Montserrat',sans-serif;color:var(--navy)}
.p{font-size:4.2px;line-height:1.5;color:var(--muted)}
.num{font:800 4px 'Montserrat',sans-serif;color:var(--navy);background:var(--orange);border-radius:5px;padding:1px 4px}
.pill{font:600 4.2px 'Montserrat',sans-serif;background:var(--orange);color:var(--navy);border-radius:6px;padding:1.5px 5px}
.bar{background:var(--navy);border-radius:4px;color:#fff}
svg{position:absolute}
</style>
</head>
<body>

<!-- 01 Cover -->
<section class="s" style="left:35px;top:31px;background:#fff">
  <div style="left:0;right:0;top:0;height:2px;background:var(--orange)"></div>
  <div class="eb" style="left:0;right:0;top:56px;text-align:center">Outsourced Franchise Sales &amp; Growth Experts</div>
  <div style="left:0;right:0;top:76px;text-align:center;font:800 19px 'Montserrat',sans-serif;color:var(--navy);letter-spacing:.01em">OUTPOST LATTICE</div>
  <div style="left:94px;top:106px;width:66px;border-top:1px solid var(--orange)"></div>
  <div style="left:324px;top:106px;width:66px;border-top:1px solid var(--orange)"></div>
  <div style="left:0;right:0;top:101px;text-align:center;font:800 10px 'Montserrat',sans-serif;color:var(--navy);letter-spacing:.45em">ADVISORS</div>
  <div class="lead" style="left:110px;right:110px;top:122px;text-align:center;font-size:5.4px">Helping franchisors grow faster without the cost and risk of building an internal franchise development team.</div>
  <div class="rule" style="left:233px;top:149px"></div>
  <div style="left:128px;top:170px;width:228px;height:26px;display:grid;grid-template-columns:repeat(3,1fr)">
    <div class="flow" style="text-align:center;border-right:1px solid var(--line)"><div style="font:700 11px 'Montserrat';color:var(--navy)">30<span style="color:var(--orange)">+</span></div><div style="font:600 3.8px 'Montserrat';letter-spacing:.1em;color:var(--muted)">YEARS EXPERIENCE</div></div>
    <div class="flow" style="text-align:center;border-right:1px solid var(--line)"><div style="font:700 11px 'Montserrat';color:var(--navy)">500<span style="color:var(--orange)">+</span></div><div style="font:600 3.8px 'Montserrat';letter-spacing:.1em;color:var(--muted)">UNITS SOLD</div></div>
    <div class="flow" style="text-align:center"><div style="font:700 11px 'Montserrat';color:var(--navy)">6</div><div style="font:600 3.8px 'Montserrat';letter-spacing:.1em;color:var(--muted)">BROKER NETWORKS</div></div>
  </div>
  <div style="left:27px;right:27px;top:252px;border-top:1px solid var(--line)"></div>
  <div style="left:0;right:0;top:248px;text-align:center"><span style="position:static;background:#fff;padding:0 6px;font:600 4.2px 'Montserrat';letter-spacing:.1em;color:#8a93a3">WWW.OUTPOSTLATTICEADVISORS.EXAMPLE · CONFIDENTIAL</span></div>
</section>

<!-- 02 Agenda -->
<section class="s" style="left:313px;top:31px">
  <div class="eb">02 · Outpost Lattice Advisors</div>
  <h2 class="t">Our <em>Agenda</em></h2>
  <div class="rule" style="left:27px;top:53px"></div>
  <div class="flow" style="position:absolute;left:208px;top:42px;width:240px;display:flex;flex-direction:column;gap:4px">
    <div class="flow" style="height:36px;background:var(--pill);border-radius:4px;display:flex;align-items:center;gap:8px;padding:0 8px"><span class="ring" style="position:relative"></span><span class="h" style="font-size:5.8px">Challenges For Emerging Franchisors</span></div>
    <div class="flow" style="height:36px;background:var(--pill);border-radius:4px;display:flex;align-items:center;gap:8px;padding:0 8px"><span class="ring" style="position:relative"></span><span class="h" style="font-size:5.8px">Internal Franchise Development vs Fractional</span></div>
    <div class="flow" style="height:36px;background:var(--pill);border-radius:4px;display:flex;align-items:center;gap:8px;padding:0 8px"><span class="ring" style="position:relative"></span><span class="h" style="font-size:5.8px">Who is Outpost Lattice Advisors</span></div>
    <div class="flow" style="height:36px;background:var(--pill);border-radius:4px;display:flex;align-items:center;gap:8px;padding:0 8px"><span class="ring" style="position:relative"></span><span class="h" style="font-size:5.8px">Growth &amp; Exit Strategy</span></div>
    <div class="flow" style="height:36px;background:var(--pill);border-radius:4px;display:flex;align-items:center;gap:8px;padding:0 8px"><span class="ring" style="position:relative"></span><span class="h" style="font-size:5.8px">Why Outpost Lattice Advisors</span></div>
  </div>
  <footer class="foot"><span>OUTPOST LATTICE ADVISORS</span><span>CONFIDENTIAL</span><span>02 / 19</span></footer>
</section>

<!-- 03 Problem -->
<section class="s" style="left:591px;top:31px">
  <div class="eb">03 · The Problem</div>
  <h2 class="t">The Challenge Facing<br><em>Emerging</em> Franchisors</h2>
  <div class="rule" style="left:27px;top:69px"></div>
  <div class="lead" style="left:27px;top:78px;width:180px">Most emerging franchisors are stuck in the same six traps — and each one quietly caps their growth ceiling.</div>
  <div style="left:27px;top:108px;padding:3px 6px;background:#fbecd2;border-radius:2px;font:600 4.6px 'Montserrat';color:var(--muted);letter-spacing:.05em">▮ 6 SILENT GROWTH CEILINGS</div>
  <div style="left:27px;top:136px"><div class="flow" style="font:700 9px 'Montserrat';color:var(--navy)">48<span style="color:var(--orange)">h</span></div><div class="flow" style="font:600 3.6px 'Montserrat';color:var(--muted);letter-spacing:.08em">LEAD DECAY WINDOW</div></div>
  <div style="left:110px;top:136px"><div class="flow" style="font:700 9px 'Montserrat';color:var(--navy)">$200K<span style="color:var(--orange)">+</span></div><div class="flow" style="font:600 3.6px 'Montserrat';color:var(--muted);letter-spacing:.08em">LOADED COMP / YR</div></div>
  <div class="flow" style="position:absolute;left:215px;top:38px;width:265px;display:flex;flex-direction:column;gap:8px">
    <div class="flow card" style="height:22px;display:flex;align-items:center;gap:7px;padding:0 6px"><span class="ic" style="position:relative;flex:none"></span><div class="flow"><div class="flow h" style="font-size:4.6px">Limited Sales Resources</div><div class="flow p" style="font-size:3.7px">No dedicated franchise sales bench; founder handles leads personally.</div></div></div>
    <div class="flow card" style="height:22px;display:flex;align-items:center;gap:7px;padding:0 6px"><span class="ic" style="position:relative;flex:none"></span><div class="flow"><div class="flow h" style="font-size:4.6px">Founder Wearing Too Many Hats</div><div class="flow p" style="font-size:3.7px">Sales, ops, finance, marketing — all on one pair of shoulders.</div></div></div>
    <div class="flow card" style="height:22px;display:flex;align-items:center;gap:7px;padding:0 6px"><span class="ic" style="position:relative;flex:none"></span><div class="flow"><div class="flow h" style="font-size:4.6px">Inconsistent Lead Follow-Up</div><div class="flow p" style="font-size:3.7px">Speed-to-lead suffers; qualified candidates go cold within 48 hours.</div></div></div>
    <div class="flow card" style="height:22px;display:flex;align-items:center;gap:7px;padding:0 6px"><span class="ic" style="position:relative;flex:none"></span><div class="flow"><div class="flow h" style="font-size:4.6px">Difficulty Recruiting Franchisees</div><div class="flow p" style="font-size:3.7px">Limited reach into broker and consultant channels.</div></div></div>
    <div class="flow card" style="height:22px;display:flex;align-items:center;gap:7px;padding:0 6px"><span class="ic" style="position:relative;flex:none"></span><div class="flow"><div class="flow h" style="font-size:4.6px">No Broker Relationships</div><div class="flow p" style="font-size:3.7px">Zero presence in Halden, KBN, TBA, Corvane ecosystems.</div></div></div>
    <div class="flow card" style="height:22px;display:flex;align-items:center;gap:7px;padding:0 6px"><span class="ic" style="position:relative;flex:none"></span><div class="flow"><div class="flow h" style="font-size:4.6px">High Cost of Internal Staff</div><div class="flow p" style="font-size:3.7px">Salary, benefits and ramp time long before the first award.</div></div></div>
  </div>
  <footer class="foot"><span>OUTPOST LATTICE ADVISORS</span><span>CONFIDENTIAL</span><span>03 / 19</span></footer>
</section>

<!-- 04 Solution -->
<section class="s" style="left:35px;top:196px">
  <div class="eb">04 · The Solution</div>
  <h2 class="t">Why <em>Outpost</em><br>Lattice Advisors</h2>
  <div class="rule" style="left:27px;top:68px"></div>
  <div class="lead" style="left:223px;top:38px;width:230px">A fractional franchise sales team that plugs into your brand on Day One — with the systems, relationships, and execution record of a 30-year franchise development organization.</div>
  <div class="flow" style="position:absolute;left:27px;top:88px;width:422px;display:grid;grid-template-columns:repeat(3,1fr);grid-template-rows:74px 74px;gap:8px">
    <div class="flow card" style="padding:8px"><span class="num">01</span><div class="flow h" style="margin-top:8px">Fractional Sales Team</div><div class="flow p" style="margin-top:3px">A full franchise development team at a fraction of internal-hire cost. Scale up or down as your pipeline demands.</div></div>
    <div class="flow card" style="padding:8px"><span class="num">02</span><div class="flow h" style="margin-top:8px">30+ Years Experience</div><div class="flow p" style="margin-top:3px">Three decades of franchise sales leadership across emerging and established systems.</div></div>
    <div class="flow navy" style="padding:8px;border-radius:4px"><span class="num">03</span><div class="flow h" style="margin-top:8px;color:#fff">500+ Sales Closed</div><div class="flow p" style="margin-top:3px;color:#c3cbd8">Over five hundred franchise units sold across multiple brands and categories. A repeatable, proven motion.</div></div>
    <div class="flow card" style="padding:8px"><span class="num">04</span><div class="flow h" style="margin-top:8px">Immediate Execution</div><div class="flow p" style="margin-top:3px">No recruiting, no ramp-up, no learning curve. We launch your development program within weeks.</div></div>
    <div class="flow card" style="padding:8px"><span class="num">05</span><div class="flow h" style="margin-top:8px">Proven Systems</div><div class="flow p" style="margin-top:3px">Documented qualification, education, FDD, validation and Discovery Day workflows.</div></div>
    <div class="flow card" style="padding:8px"><span class="num">06</span><div class="flow h" style="margin-top:8px">Deep Broker Network</div><div class="flow p" style="margin-top:3px">Established, trusted relationships with every major franchise broker network in North America.</div></div>
  </div>
  <footer class="foot"><span>OUTPOST LATTICE ADVISORS</span><span>CONFIDENTIAL</span><span>04 / 19</span></footer>
</section>

<!-- 05 Hire vs outsource -->
<section class="s" style="left:313px;top:196px">
  <div class="eb">05 · Hire vs. Outsource</div>
  <h2 class="t">The Cost of Hiring<br><em>vs. Outsourcing</em></h2>
  <div class="rule" style="left:27px;top:68px"></div>
  <div class="lead" style="left:256px;top:38px;width:200px">A single internal director carries hidden costs the org chart never shows. OLA replaces all of it with one fractional investment.</div>
  <div class="card" style="left:27px;top:84px;width:196px;height:160px;border:1px solid #9aa5b8">
    <div style="left:0;right:0;top:0;height:28px;background:var(--pill);border-radius:4px 4px 0 0"></div>
    <div class="h" style="left:8px;top:6px;font-size:4.8px">Internal Franchise Development Director</div>
    <div class="p" style="left:8px;top:15px;font-size:3.6px">All-in cost of one full-time hire</div>
    <div style="right:7px;top:7px;font:700 3.2px 'Montserrat';background:#fbe3bd;color:var(--orange);padding:1px 3px;border-radius:3px">INTERNAL HIRE</div>
    <div class="flow p" style="position:absolute;left:8px;top:36px;right:8px;display:flex;flex-direction:column;gap:5.6px;font-size:3.9px;color:var(--ink)">
      <div class="flow">01 &nbsp;✕&nbsp; Recruiting costs (15–25% of first-year salary)</div>
      <div class="flow">02 &nbsp;✕&nbsp; Base salary ($140K–$180K)</div>
      <div class="flow">03 &nbsp;✕&nbsp; Benefits &amp; PTO (25–30% load)</div>
      <div class="flow">04 &nbsp;✕&nbsp; Payroll taxes</div>
      <div class="flow">05 &nbsp;✕&nbsp; Training &amp; onboarding</div>
      <div class="flow">06 &nbsp;✕&nbsp; 6–9 month ramp-up period</div>
      <div class="flow">07 &nbsp;✕&nbsp; Unknown performance / hit-or-miss</div>
    </div>
  </div>
  <div style="left:227px;top:152px;width:20px;height:20px;border-radius:50%;border:1px solid var(--orange);background:#fff;text-align:center;font:italic 700 5px/18px 'Montserrat';color:var(--navy)">vs</div>
  <div class="card" style="left:252px;top:84px;width:196px;height:160px;border:1px solid var(--navy)">
    <div style="left:0;right:0;top:0;height:28px;background:var(--navy);border-radius:3px 3px 0 0"></div>
    <div class="h" style="left:8px;top:6px;font-size:4.8px;color:#fff">Outpost Lattice Advisors</div>
    <div class="p" style="left:8px;top:15px;font-size:3.6px;color:#c3cbd8">Fractional investment, entire team</div>
    <div style="right:7px;top:7px;font:700 3.2px 'Montserrat';background:var(--orange);color:var(--navy);padding:1px 3px;border-radius:3px">OLA</div>
    <div class="flow p" style="position:absolute;left:8px;top:38px;right:8px;display:flex;flex-direction:column;gap:6.4px;font-size:3.9px;color:var(--ink)">
      <div class="flow">01 &nbsp;<span style="color:var(--orange)">✓</span>&nbsp; Fractional investment (sub-director cost)</div>
      <div class="flow">02 &nbsp;<span style="color:var(--orange)">✓</span>&nbsp; Entire team of franchise sales experts</div>
      <div class="flow">03 &nbsp;<span style="color:var(--orange)">✓</span>&nbsp; Immediate launch — no ramp-up</div>
      <div class="flow">04 &nbsp;<span style="color:var(--orange)">✓</span>&nbsp; Proven, documented processes</div>
      <div class="flow">05 &nbsp;<span style="color:var(--orange)">✓</span>&nbsp; Existing broker relationships</div>
      <div class="flow">06 &nbsp;<span style="color:var(--orange)">✓</span>&nbsp; Scalable growth — flex up or down</div>
    </div>
  </div>
  <footer class="foot"><span>OUTPOST LATTICE ADVISORS</span><span>CONFIDENTIAL</span><span>05 / 19</span></footer>
</section>

<!-- 06 Capabilities -->
<section class="s" style="left:591px;top:196px">
  <div class="eb">06 · Day-One Capabilities</div>
  <h2 class="t">What Takes Years to Build,<br>You Get on <em>Day One</em></h2>
  <div class="rule" style="left:27px;top:68px"></div>
  <div style="left:27px;top:83px;font:700 3.8px 'Montserrat';color:var(--orange);letter-spacing:.08em">INHERITED CAPABILITIES</div>
  <div class="flow" style="position:absolute;left:27px;top:96px;width:230px;display:grid;grid-template-columns:1fr 1fr;row-gap:9px;column-gap:10px">
    <div class="flow" style="display:flex;gap:4px;align-items:center;border-bottom:1px solid var(--line);padding-bottom:3px"><span class="num" style="position:relative;background:var(--navy);color:#fff;padding:1px 2px">1</span><span class="ring" style="position:relative"></span><div class="flow"><div class="flow h" style="font-size:3.9px">Broker Relationships</div><div class="flow p" style="font-size:3.2px">HANDSHAKE</div></div></div>
    <div class="flow" style="display:flex;gap:4px;align-items:center;border-bottom:1px solid var(--line);padding-bottom:3px"><span class="num" style="position:relative;background:var(--navy);color:#fff;padding:1px 2px">5</span><span class="ring" style="position:relative"></span><div class="flow"><div class="flow h" style="font-size:3.9px">Industry Connections</div><div class="flow p" style="font-size:3.2px">HUB</div></div></div>
    <div class="flow" style="display:flex;gap:4px;align-items:center;border-bottom:1px solid var(--line);padding-bottom:3px"><span class="num" style="position:relative;background:var(--navy);color:#fff;padding:1px 2px">2</span><span class="ring" style="position:relative"></span><div class="flow"><div class="flow h" style="font-size:3.9px">Sales Expertise</div><div class="flow p" style="font-size:3.2px">PSYCHOLOGY</div></div></div>
    <div class="flow" style="display:flex;gap:4px;align-items:center;border-bottom:1px solid var(--line);padding-bottom:3px"><span class="num" style="position:relative;background:var(--navy);color:#fff;padding:1px 2px">6</span><span class="ring" style="position:relative"></span><div class="flow"><div class="flow h" style="font-size:3.9px">Candidate Nurturing</div><div class="flow p" style="font-size:3.2px">FAVORITE</div></div></div>
    <div class="flow" style="display:flex;gap:4px;align-items:center;border-bottom:1px solid var(--line);padding-bottom:3px"><span class="num" style="position:relative;background:var(--navy);color:#fff;padding:1px 2px">3</span><span class="ring" style="position:relative"></span><div class="flow"><div class="flow h" style="font-size:3.9px">Lead Qualification Systems</div><div class="flow p" style="font-size:3.2px">FILTER</div></div></div>
    <div class="flow" style="display:flex;gap:4px;align-items:center;border-bottom:1px solid var(--line);padding-bottom:3px"><span class="num" style="position:relative;background:var(--navy);color:#fff;padding:1px 2px">7</span><span class="ring" style="position:relative"></span><div class="flow"><div class="flow h" style="font-size:3.9px">CRM &amp; Reporting</div><div class="flow p" style="font-size:3.2px">ANALYTICS</div></div></div>
    <div class="flow" style="display:flex;gap:4px;align-items:center;border-bottom:1px solid var(--line);padding-bottom:3px"><span class="num" style="position:relative;background:var(--navy);color:#fff;padding:1px 2px">4</span><span class="ring" style="position:relative"></span><div class="flow"><div class="flow h" style="font-size:3.9px">Development Processes</div><div class="flow p" style="font-size:3.2px">ROUTE</div></div></div>
  </div>
  <div class="lead" style="left:272px;top:33px;width:180px;font-size:4.8px">Seven interlocking capabilities, refined over three decades of franchise development, plug into your brand on engagement.</div>
  <div class="navy" style="left:272px;top:80px;width:96px;height:150px;border-radius:4px">
    <div style="left:8px;top:6px;font:800 15px 'Montserrat';color:#fff">7<span style="color:var(--orange)">.</span></div>
    <div style="left:8px;top:29px;font:600 3.6px 'Montserrat';letter-spacing:.05em;color:#c3cbd8">CAPABILITIES INHERITED</div>
    <div style="left:8px;right:8px;top:38px;border-top:1px solid #36507a"></div>
    <div style="left:8px;top:45px;font:800 10px 'Montserrat';color:var(--orange)">30+</div>
    <div style="left:8px;top:62px;font:600 3.6px 'Montserrat';color:#c3cbd8">YEARS REFINING</div>
    <div style="left:8px;right:8px;top:71px;border-top:1px solid #36507a"></div>
    <div style="left:8px;top:76px;font:800 10px 'Montserrat';color:#fff">Day 1</div>
    <div style="left:8px;top:93px;font:600 3.6px 'Montserrat';color:#c3cbd8">ACTIVATION</div>
    <div style="left:8px;right:8px;top:102px;border-top:1px solid #36507a"></div>
    <div style="left:8px;top:110px;font:600 3.6px 'Montserrat';color:#c3cbd8">COMPOUNDING</div>
  </div>
  <footer class="foot"><span>OUTPOST LATTICE ADVISORS</span><span>CONFIDENTIAL</span><span>06 / 19</span></footer>
</section>

<!-- 07 Broker ecosystem -->
<section class="s" style="left:35px;top:359px">
  <div class="eb">07 · Broker Ecosystem</div>
  <h2 class="t">Instant Access to the<br><em>Franchise Broker</em> Community</h2>
  <div class="rule" style="left:27px;top:68px"></div>
  <div class="lead" style="left:265px;top:28px;width:185px">We spent 20+ years building these relationships so your brand doesn't have to. OLA sits at the center of the broker ecosystem.</div>
  <svg width="484" height="272" viewBox="0 0 484 272" style="left:0;top:0">
    <g stroke="var(--orange)" stroke-width=".7" fill="none">
      <path d="M165 96 H210 V118"/><path d="M276 118 V96 H318"/>
      <path d="M132 145 H210"/><path d="M276 145 H360"/>
      <path d="M185 190 H232 V172"/><path d="M254 172 V190 H315"/>
    </g>
  </svg>
  <div style="left:209px;top:104px;width:68px;height:68px;border-radius:50%;background:var(--navy);text-align:center">
    <div class="flow" style="margin-top:16px;font:700 5.8px/1.25 'Montserrat';color:#fff">Outpost<br>Lattice<br>Advisors</div>
    <div class="flow" style="margin-top:3px;font:600 3.6px/1.3 'Montserrat';letter-spacing:.1em;color:#c3cbd8">ECOSYSTEM<br>HUB</div>
  </div>
  <div class="card" style="left:100px;top:80px;width:66px;height:32px;text-align:center"><span class="pill" style="position:relative;top:-3px">KBN</span><div class="flow p" style="font-size:3.6px;margin-top:-1px">Keystone Broker<br>Network</div></div>
  <div class="card" style="left:318px;top:80px;width:62px;height:32px;text-align:center"><span class="pill" style="position:relative;top:-3px">TGP</span><div class="flow p" style="font-size:3.6px;margin-top:-1px">The Growth Pool /<br>network</div></div>
  <div class="card" style="left:62px;top:128px;width:70px;height:32px;text-align:center"><span class="pill" style="position:relative;top:-3px">HALDEN</span><div class="flow p" style="font-size:3.6px;margin-top:-1px">Independent Franchise<br>Professionals Group</div></div>
  <div class="card" style="left:360px;top:127px;width:66px;height:34px;text-align:center"><span class="pill" style="position:relative;top:-3px">NWB</span><div class="flow p" style="font-size:3.6px;margin-top:-1px">Northwind / franchise<br>brokers</div></div>
  <div class="card" style="left:118px;top:172px;width:68px;height:34px;text-align:center"><span class="pill" style="position:relative;top:-3px">CORVANE</span><div class="flow p" style="font-size:3.6px;margin-top:-1px">Franchise matching &amp;<br>referral</div></div>
  <div class="card" style="left:315px;top:175px;width:66px;height:32px;text-align:center"><span class="pill" style="position:relative;top:-3px">TBA</span><div class="flow p" style="font-size:3.6px;margin-top:-1px">Trusted broker<br>alliance</div></div>
  <div style="left:27px;right:27px;top:240px;border-top:1px solid var(--orange)"></div>
  <div style="left:0;right:0;top:235px;text-align:center"><span style="position:static;background:var(--slide);padding:0 6px;font:italic 4.4px 'Open Sans';color:var(--ink)">We spent <b style="color:var(--orange)">20+ years</b> building these relationships so your brand doesn't have to.</span></div>
  <footer class="foot"><span>OUTPOST LATTICE ADVISORS</span><span>CONFIDENTIAL</span><span>07 / 19</span></footer>
</section>

<!-- 08 Process -->
<section class="s" style="left:313px;top:359px">
  <div class="eb" style="left:0;right:0;text-align:center;top:24px">08 · The Process</div>
  <h2 class="t" style="left:0;right:0;top:33px;text-align:center">Our Franchise <em>Development</em> Process</h2>
  <div class="lead" style="left:0;right:0;top:60px;text-align:center">A seven-stage funnel that takes a cold lead from first touch to signed franchise award — engineered for conversion at every step.</div>
  <div style="left:35px;right:35px;top:122px;border-top:1px solid #b9c1cf"></div>
  <div class="flow" style="position:absolute;left:22px;right:22px;top:117px;display:grid;grid-template-columns:repeat(7,1fr);text-align:center">
    <div class="flow"><div class="flow" style="margin:0 auto;width:10px;height:10px;border-radius:50%;border:1px solid var(--navy);background:#fff;font:700 3.6px/8px 'Montserrat'">01</div><div class="flow" style="margin:5px 2px 0;background:var(--pill);font:700 4px/10px 'Montserrat';color:var(--navy)">Lead</div><div class="flow p" style="margin-top:5px;font-size:3.6px">Inbound &amp;<br>broker-sourced</div></div>
    <div class="flow"><div class="flow" style="margin:0 auto;width:10px;height:10px;border-radius:50%;border:1px solid var(--navy);background:#fff;font:700 3.6px/8px 'Montserrat'">02</div><div class="flow" style="margin:5px 2px 0;background:var(--pill);font:700 4px/10px 'Montserrat';color:var(--navy)">Qualification</div><div class="flow p" style="margin-top:5px;font-size:3.6px">Fit, finance,<br>timing</div></div>
    <div class="flow"><div class="flow" style="margin:0 auto;width:10px;height:10px;border-radius:50%;border:1px solid var(--navy);background:#fff;font:700 3.6px/8px 'Montserrat'">03</div><div class="flow" style="margin:5px 2px 0;background:var(--pill);font:700 4px/10px 'Montserrat';color:var(--navy)">Education</div><div class="flow p" style="margin-top:5px;font-size:3.6px">Brand &amp; unit<br>economics</div></div>
    <div class="flow"><div class="flow" style="margin:0 auto;width:10px;height:10px;border-radius:50%;border:1px solid var(--navy);background:#fff;font:700 3.6px/8px 'Montserrat'">04</div><div class="flow" style="margin:5px 2px 0;background:var(--pill);font:700 4px/10px 'Montserrat';color:var(--navy)">FDD Review</div><div class="flow p" style="margin-top:5px;font-size:3.6px">Disclosure &amp;<br>legal</div></div>
    <div class="flow"><div class="flow" style="margin:0 auto;width:10px;height:10px;border-radius:50%;border:1px solid var(--navy);background:#fff;font:700 3.6px/8px 'Montserrat'">05</div><div class="flow" style="margin:5px 2px 0;background:var(--pill);font:700 4px/10px 'Montserrat';color:var(--navy)">Validation</div><div class="flow p" style="margin-top:5px;font-size:3.6px">Franchisee<br>reference calls</div></div>
    <div class="flow"><div class="flow" style="margin:0 auto;width:10px;height:10px;border-radius:50%;border:1px solid var(--navy);background:#fff;font:700 3.6px/8px 'Montserrat'">06</div><div class="flow" style="margin:5px 2px 0;background:var(--pill);font:700 4px/10px 'Montserrat';color:var(--navy)">Discovery Day</div><div class="flow p" style="margin-top:5px;font-size:3.6px">Final mutual<br>fit</div></div>
    <div class="flow"><div class="flow" style="margin:0 auto;width:10px;height:10px;border-radius:50%;border:1px solid var(--navy);background:#fff;font:700 3.6px/8px 'Montserrat'">07</div><div class="flow" style="margin:5px 2px 0;background:var(--pill);font:700 4px/10px 'Montserrat';color:var(--navy)">Franchise Award</div><div class="flow p" style="margin-top:5px;font-size:3.6px">Signed &amp;<br>welcomed</div></div>
  </div>
  <div style="left:130px;width:228px;top:184px;height:24px;border-radius:12px;background:#dde2ea;text-align:center;font:italic 600 5px/24px 'Open Sans';color:var(--navy)">Average cycle: 60–120 days from first contact to award.</div>
  <footer class="foot"><span>OUTPOST LATTICE ADVISORS</span><span>CONFIDENTIAL</span><span>08 / 19</span></footer>
</section>

<!-- 09 Services -->
<section class="s" style="left:591px;top:359px">
  <div class="eb">09 · Services</div>
  <h2 class="t">Services <em>We Provide</em></h2>
  <div class="rule" style="left:27px;top:50px"></div>
  <div class="lead" style="left:27px;top:56px;width:300px">End-to-end franchise development — sold as an integrated engagement or scoped to fill the gap in your existing team.</div>
  <div class="flow" style="position:absolute;left:27px;top:86px;width:432px;display:grid;grid-template-columns:repeat(4,1fr);grid-template-rows:74px 74px;gap:8px">
    <div class="flow card" style="padding:8px"><span class="ic" style="position:relative;display:block"></span><div class="flow h" style="margin-top:6px;font-size:4.6px">FDD / Operations Review</div><div class="flow p" style="margin-top:2px;font-size:3.6px">Audit of your Franchise Disclosure Document and operating model. Identify friction points before brokers do.</div></div>
    <div class="flow card" style="padding:8px"><span class="ic" style="position:relative;display:block"></span><div class="flow h" style="margin-top:6px;font-size:4.6px">Franchise Sales Outsourcing</div><div class="flow p" style="margin-top:2px;font-size:3.6px">Full-cycle sales execution from lead intake to award. We become your franchise development team.</div></div>
    <div class="flow card" style="padding:8px"><span class="ic" style="position:relative;display:block"></span><div class="flow h" style="margin-top:6px;font-size:4.6px">Lead Qualification</div><div class="flow p" style="margin-top:2px;font-size:3.6px">Score, screen, and route every candidate. Disqualify early so your team only meets serious buyers.</div></div>
    <div class="flow card" style="padding:8px"><span class="ic" style="position:relative;display:block"></span><div class="flow h" style="margin-top:6px;font-size:4.6px">Candidate Nurturing</div><div class="flow p" style="margin-top:2px;font-size:3.6px">Multi-touch follow-up across email, phone, video. Keep qualified candidates advancing through the funnel.</div></div>
    <div class="flow card" style="padding:8px"><span class="ic" style="position:relative;display:block"></span><div class="flow h" style="margin-top:6px;font-size:4.6px">Discovery Day Coordination</div><div class="flow p" style="margin-top:2px;font-size:3.6px">Plan, schedule, and facilitate your final-round candidate day. We manage logistics; you close.</div></div>
    <div class="flow card" style="padding:8px"><span class="ic" style="position:relative;display:block"></span><div class="flow h" style="margin-top:6px;font-size:4.6px">Broker Recruitment</div><div class="flow p" style="margin-top:2px;font-size:3.6px">Activate new broker partners and keep existing ones trained on your brand. Your deal flow compounds.</div></div>
    <div class="flow card" style="padding:8px"><span class="ic" style="position:relative;display:block"></span><div class="flow h" style="margin-top:6px;font-size:4.6px">CRM Management</div><div class="flow p" style="margin-top:2px;font-size:3.6px">Pipeline hygiene, stage definitions, and reporting cadence. A clean CRM is a forecastable pipeline.</div></div>
    <div class="flow card" style="padding:8px"><span class="ic" style="position:relative;display:block"></span><div class="flow h" style="margin-top:6px;font-size:4.6px">Reporting &amp; Forecasting</div><div class="flow p" style="margin-top:2px;font-size:3.6px">Weekly activity, monthly close rate, quarterly forecast. You always know what is in the pipe.</div></div>
  </div>
  <footer class="foot"><span>OUTPOST LATTICE ADVISORS</span><span>CONFIDENTIAL</span><span>09 / 19</span></footer>
</section>

<!-- 10 Referral engine -->
<section class="s" style="left:35px;top:523px">
  <div class="eb">10 · Referral Engine</div>
  <h2 class="t" style="font-size:13px">Building a <em>Referral<br>Engine</em> for Your<br>Brand</h2>
  <div style="left:27px;top:118px;width:150px;font:italic 5px/1.5 'Open Sans';color:var(--ink)">The brands brokers remember are the brands brokers refer.</div>
  <div class="lead" style="left:27px;top:142px;width:150px">Franchise brokers drive 40–60% of new unit sales in mature systems. We turn your brand into a broker favorite through structured education, communication, and ongoing engagement.</div>
  <div class="flow" style="position:absolute;left:198px;top:42px;width:250px;display:flex;flex-direction:column;gap:8px">
    <div class="flow" style="height:36px;background:var(--pill);border-radius:4px;display:flex;align-items:center;gap:7px;padding:0 8px"><span class="flow" style="width:16px;height:16px;border-radius:50%;background:var(--navy);flex:none"></span><div class="flow"><div class="flow h" style="font-size:4.8px">Broker/Consultant education</div><div class="flow p" style="font-size:3.8px">Structured onboarding sessions that get every broker fluent in your brand, model, and ideal candidate.</div></div></div>
    <div class="flow" style="height:36px;background:var(--pill);border-radius:4px;display:flex;align-items:center;gap:7px;padding:0 8px"><span class="flow" style="width:16px;height:16px;border-radius:50%;background:var(--navy);flex:none"></span><div class="flow"><div class="flow h" style="font-size:4.8px">Brand Presentations</div><div class="flow p" style="font-size:3.8px">Live and recorded brand showcases for broker networks — your story, told the right way, at scale.</div></div></div>
    <div class="flow" style="height:36px;background:var(--pill);border-radius:4px;display:flex;align-items:center;gap:7px;padding:0 8px"><span class="flow" style="width:16px;height:16px;border-radius:50%;background:var(--navy);flex:none"></span><div class="flow"><div class="flow h" style="font-size:4.8px">Ongoing Communication</div><div class="flow p" style="font-size:3.8px">Quarterly broker updates, deal reviews, and incentive programs that keep your brand top-of-mind.</div></div></div>
    <div class="flow" style="height:36px;background:var(--pill);border-radius:4px;display:flex;align-items:center;gap:7px;padding:0 8px"><span class="flow" style="width:16px;height:16px;border-radius:50%;background:var(--navy);flex:none"></span><div class="flow"><div class="flow h" style="font-size:4.8px">Referral Generation</div><div class="flow p" style="font-size:3.8px">Tiered broker incentives and recognition that reward brokers for sending qualified candidates.</div></div></div>
  </div>
  <footer class="foot"><span>OUTPOST LATTICE ADVISORS</span><span>CONFIDENTIAL</span><span>10 / 19</span></footer>
</section>

<!-- 11 Track record -->
<section class="s" style="left:313px;top:523px">
  <div class="eb">11 · Track Record</div>
  <h2 class="t">Why <em>Experience Matters</em></h2>
  <div class="rule" style="left:27px;top:50px"></div>
  <div class="lead" style="left:27px;top:59px;width:420px">Three decades of franchise sales leadership translate into pattern recognition, broker trust, and a candidate pipeline that compounds.</div>
  <div class="flow" style="position:absolute;left:20px;top:78px;width:444px;display:grid;grid-template-columns:repeat(5,1fr);gap:4px;height:150px">
    <div class="flow card" style="text-align:center;padding:10px 4px;position:relative"><div class="flow" style="font:700 15px 'Montserrat';color:var(--navy)">500+</div><div class="flow h" style="font-size:3.6px;margin-top:8px">FRANCHISE SALES<br>SUCCESSES</div><div class="flow p" style="font-size:3.5px;margin-top:6px">Closed across multiple brands and categories over our history.</div><div class="abs" style="left:50%;margin-left:-7px;bottom:8px;width:14px;height:14px;border-radius:50%;background:#e8ebf0"></div></div>
    <div class="flow card" style="text-align:center;padding:10px 4px;position:relative"><div class="flow" style="font:700 15px 'Montserrat';color:var(--navy)">30+</div><div class="flow h" style="font-size:3.6px;margin-top:8px">YEARS INDUSTRY<br>EXPERIENCE</div><div class="flow p" style="font-size:3.5px;margin-top:6px">Three decades of franchise development leadership, every cycle seen.</div><div class="abs" style="left:50%;margin-left:-7px;bottom:8px;width:14px;height:14px;border-radius:50%;background:#e8ebf0"></div></div>
    <div class="flow card" style="text-align:center;padding:10px 4px;position:relative"><div class="flow" style="font:700 15px 'Montserrat';color:var(--navy)">10K+</div><div class="flow h" style="font-size:3.6px;margin-top:8px">FRANCHISE CANDIDATES<br>EVALUATED</div><div class="flow p" style="font-size:3.5px;margin-top:6px">Thousands of franchise candidates screened and qualified.</div><div class="abs" style="left:50%;margin-left:-7px;bottom:8px;width:14px;height:14px;border-radius:50%;background:#e8ebf0"></div></div>
    <div class="flow card" style="text-align:center;padding:10px 4px;position:relative"><div class="flow" style="font:700 15px 'Montserrat';color:var(--navy)">6</div><div class="flow h" style="font-size:3.6px;margin-top:8px">BROKER NETWORK<br>RELATIONSHIPS</div><div class="flow p" style="font-size:3.5px;margin-top:6px">Halden, KBN, TGP, TBA, NWB, Corvane — direct, active relationships.</div><div class="abs" style="left:50%;margin-left:-7px;bottom:8px;width:14px;height:14px;border-radius:50%;background:#e8ebf0"></div></div>
    <div class="flow card" style="text-align:center;padding:10px 4px;position:relative"><div class="flow" style="font:700 14px 'Montserrat';color:var(--navy)">Multi</div><div class="flow h" style="font-size:3.6px;margin-top:9px">BRAND DEVELOPMENT<br>EXPERTISE</div><div class="flow p" style="font-size:3.5px;margin-top:6px">Franchise development across QSR, services, retail, fitness, and home-based.</div><div class="abs" style="left:50%;margin-left:-7px;bottom:8px;width:14px;height:14px;border-radius:50%;background:#e8ebf0"></div></div>
  </div>
  <footer class="foot"><span>OUTPOST LATTICE ADVISORS</span><span>CONFIDENTIAL</span><span>11 / 19</span></footer>
</section>

<!-- 12 Success stories -->
<section class="s" style="left:591px;top:523px">
  <div class="eb">12 · Proof</div>
  <h2 class="t">Success <em>Stories</em></h2>
  <div class="rule" style="left:27px;top:50px"></div>
  <div class="lead" style="left:27px;top:56px;width:420px">Three representative engagements across emerging, growth-stage, and multi-brand franchise systems.</div>
  <div class="flow" style="position:absolute;left:27px;top:80px;width:430px;display:grid;grid-template-columns:repeat(3,1fr);gap:6px">
    <div class="flow card" style="height:58px;padding:5px 6px;position:relative"><div class="flow" style="font:700 2.8px 'Montserrat';color:var(--orange)">CASE STUDY 01</div><div class="flow h" style="font-size:4.2px;margin-top:1px">Emerging<br>Franchise System</div><div class="abs" style="right:6px;top:4px;text-align:right"><div style="font:700 7.5px 'Montserrat';color:var(--navy)">12</div><div style="font:700 2.8px 'Montserrat';color:var(--orange)">UNITS YEAR 1–2</div></div><div class="flow" style="border-top:1px solid var(--line);margin-top:6px;padding-top:4px;font-size:3.5px;color:var(--muted);line-height:1.6">Built broker channel from zero and closed first 12 units within 18 months of engagement.</div></div>
    <div class="flow card" style="height:58px;padding:5px 6px;position:relative"><div class="flow" style="font:700 2.8px 'Montserrat';color:var(--orange)">CASE STUDY 02</div><div class="flow h" style="font-size:4.2px;margin-top:1px">Growth-Stage<br>Brand</div><div class="abs" style="right:6px;top:4px;text-align:right"><div style="font:700 7.5px 'Montserrat';color:var(--navy)">71%</div><div style="font:700 2.8px 'Montserrat';color:var(--orange)">DISCOVERY CLOSE RATE</div></div><div class="flow" style="border-top:1px solid var(--line);margin-top:6px;padding-top:4px;font-size:3.5px;color:var(--muted);line-height:1.6">Re-engineered sales process and lifted Discovery Day close rate from 38% to 71%.</div></div>
    <div class="flow card" style="height:58px;padding:5px 6px;position:relative"><div class="flow" style="font:700 2.8px 'Montserrat';color:var(--orange)">CASE STUDY 03</div><div class="flow h" style="font-size:4.2px;margin-top:1px">Multi-Brand<br>Portfolio</div><div class="abs" style="right:6px;top:4px;text-align:right"><div style="font:700 7.5px 'Montserrat';color:var(--navy)">40+</div><div style="font:700 2.8px 'Montserrat';color:var(--orange)">UNITS / 24 MONTHS</div></div><div class="flow" style="border-top:1px solid var(--line);margin-top:6px;padding-top:4px;font-size:3.5px;color:var(--muted);line-height:1.6">Launched two new franchise concepts &amp; signed 40+ units across the portfolio in 24 months.</div></div>
  </div>
  <div style="left:150px;width:184px;top:155px;height:9px;border-radius:5px;border:1px solid var(--line);text-align:center;font:italic 3.5px/8px 'Open Sans';color:var(--muted)">Results anonymized. Detailed references available upon request.</div>
  <footer class="foot"><span>OUTPOST LATTICE ADVISORS</span><span>CONFIDENTIAL</span><span>12 / 19</span></footer>
</section>

<!-- 13 Enterprise value -->
<section class="s" style="left:35px;top:686px">
  <div class="eb">13 · Enterprise Value</div>
  <h2 class="t" style="font-size:12.5px">Building Enterprise Value Through <em>Franchise Growth</em></h2>
  <div class="rule" style="left:27px;top:50px"></div>
  <div class="lead" style="left:27px;top:62px">Franchise growth creates recurring royalty revenue and increases enterprise value.</div>
  <div class="card" style="left:27px;top:78px;width:208px;height:82px">
    <div style="left:8px;top:7px;font:700 3.6px 'Montserrat';letter-spacing:.08em;color:var(--muted)">EXAMPLE GROWTH SCENARIO</div>
    <table class="flow" style="position:absolute;left:8px;top:18px;width:192px;border-collapse:collapse;font-size:3.2px">
      <tr><th style="border:1px solid #555;text-align:left;padding:1.5px 2px;font-weight:700">STAGE</th><th style="border:1px solid #555;text-align:left;padding:1.5px 2px;font-weight:700">UNITS ANNUAL ROYALTY REVENUE</th></tr>
      <tr><td style="border:1px solid #555;padding:2px">Early Growth 20</td><td style="border:1px solid #555;padding:2px">$165,000</td></tr>
      <tr><td style="border:1px solid #555;padding:2px">Growth Stage 65</td><td style="border:1px solid #555;padding:2px">$1,470,000</td></tr>
    </table>
    <div style="left:8px;top:67px;font:italic 3.3px 'Open Sans';color:var(--muted)">Illustrative — assumes $5K avg monthly royalty per unit.</div>
  </div>
  <div class="card" style="left:243px;top:78px;width:205px;height:82px">
    <div style="left:8px;top:7px;font:700 3.6px 'Montserrat';letter-spacing:.08em;color:var(--muted)">ILLUSTRATIVE VALUATION RANGE</div>
    <table class="flow" style="position:absolute;left:8px;top:18px;width:189px;border-collapse:collapse;font-size:3.2px">
      <tr><th style="border:1px solid #555;text-align:left;padding:1.5px 2px">ROYALTY REVENUE</th><th style="border:1px solid #555;text-align:left;padding:1.5px 2px">10X EBITDA</th><th style="border:1px solid #555;text-align:left;padding:1.5px 2px">15X EBITDA</th></tr>
      <tr><td style="border:1px solid #555;padding:2px">$165,000</td><td style="border:1px solid #555;padding:2px">$1.65M</td><td style="border:1px solid #555;padding:2px">$2.48M</td></tr>
      <tr><td style="border:1px solid #555;padding:2px">$1,470,000</td><td style="border:1px solid #555;padding:2px">$14.7M</td><td style="border:1px solid #555;padding:2px">$22.05M</td></tr>
    </table>
    <div style="left:8px;top:67px;font:italic 3.3px 'Open Sans';color:var(--muted)">Multiples illustrative; actual multiples vary by category and growth profile.</div>
  </div>
  <div class="bar" style="left:13px;top:184px;width:448px;height:38px">
    <div style="left:10px;top:12px;font:700 3.4px/1.4 'Montserrat';color:var(--orange);letter-spacing:.08em">KEY<br>TAKEAWAY</div>
    <div style="left:62px;top:10px;width:360px;font:italic 4.6px/1.6 'Open Sans'">Franchise growth is not just about selling franchises — it is about creating recurring royalty revenue that can significantly increase the value of the franchise system.</div>
  </div>
  <footer class="foot"><span>OUTPOST LATTICE ADVISORS</span><span>CONFIDENTIAL</span><span>13 / 19</span></footer>
</section>

<!-- 14 Growth curve -->
<section class="s" style="left:313px;top:686px">
  <div class="eb">14 · Our Growth</div>
  <h2 class="t" style="top:28px">The Growth Curve We <em>Build Toward</em></h2>
  <div class="lead" style="left:27px;top:46px"><span style="position:static;display:inline-block;width:10px;border-top:1px solid var(--orange);vertical-align:middle;margin-right:4px"></span>Toward Disciplined development turns linear unit growth into compounding enterprise value.</div>
  <svg width="240" height="140" viewBox="0 0 240 140" style="left:18px;top:78px">
    <g font-family="Open Sans" font-size="3.6" fill="#333">
      <text x="5" y="6">160</text><text x="5" y="19">140</text><text x="5" y="32">120</text><text x="5" y="45">100</text><text x="8" y="58">80</text><text x="8" y="71">60</text><text x="8" y="84">40</text><text x="8" y="97">20</text><text x="12" y="110">0</text>
      <text x="36" y="118">1</text><text x="69" y="118">2</text><text x="102" y="118">3</text><text x="145" y="118">4</text><text x="180" y="118">5</text>
      <text x="96" y="127" fill="#999" letter-spacing="2">YEARS</text>
    </g>
    <line x1="18" y1="2" x2="18" y2="108" stroke="#333" stroke-width=".5"/>
    <line x1="18" y1="108" x2="195" y2="108" stroke="#333" stroke-width=".5"/>
    <path d="M22 106 C70 98, 110 82, 135 62 S165 25, 172 6" stroke="var(--navy)" stroke-width="1" fill="none"/>
    <g fill="var(--orange)"><circle cx="37" cy="103" r="1.2"/><circle cx="92" cy="87" r="1.2"/><circle cx="120" cy="71" r="1.2"/><circle cx="150" cy="44" r="1.2"/><circle cx="172" cy="6" r="1.2"/></g>
    <g font-family="Montserrat" font-size="3.4" font-weight="700" fill="var(--navy)"><text x="35" y="99">12</text><text x="90" y="83">31</text><text x="118" y="67">58</text><text x="148" y="40">96</text><text x="169" y="4">148</text></g>
    <line x1="173" y1="6" x2="183" y2="16" stroke="var(--orange)" stroke-width=".5"/>
    <rect x="183" y="12" width="30" height="11" rx="2" fill="#fff" stroke="var(--orange)" stroke-width=".5"/>
    <text x="187" y="18" font-family="Montserrat" font-size="4" font-weight="700" fill="var(--orange)">148 Units</text>
    <text x="190" y="21.5" font-family="Open Sans" font-size="2.2" fill="#888">Growth · 5-yr</text>
  </svg>
  <div style="left:258px;top:80px;height:150px;border-left:1px solid var(--line)"></div>
  <div class="flow" style="position:absolute;left:270px;top:78px;width:180px;display:flex;flex-direction:column;gap:7px">
    <div class="flow card" style="height:34px;display:flex;gap:6px;align-items:center;padding:0 6px"><span class="flow" style="width:14px;height:14px;border-radius:50%;background:var(--navy);flex:none"></span><div class="flow"><div class="flow h" style="font-size:4.4px">Compounding, not linear</div><div class="flow p" style="font-size:3.6px">Unit count rises steadily – enterprise value accelerates.</div></div></div>
    <div class="flow card" style="height:34px;display:flex;gap:6px;align-items:center;padding:0 6px"><span class="flow" style="width:14px;height:14px;border-radius:50%;background:var(--navy);flex:none"></span><div class="flow"><div class="flow h" style="font-size:4.4px">Recurring royalty base</div><div class="flow p" style="font-size:3.6px">Each award adds durable, high-margin revenue.</div></div></div>
    <div class="flow card" style="height:34px;display:flex;gap:6px;align-items:center;padding:0 6px"><span class="flow" style="width:14px;height:14px;border-radius:50%;background:var(--navy);flex:none"></span><div class="flow"><div class="flow h" style="font-size:4.4px">Platform Scale</div><div class="flow p" style="font-size:3.6px">System of this size enter institutional buyers' screens.</div></div></div>
  </div>
  <footer class="foot"><span>OUTPOST LATTICE ADVISORS</span><span>CONFIDENTIAL</span><span>14 / 19</span></footer>
</section>

<!-- 15 Exit strategy -->
<section class="s" style="left:591px;top:686px">
  <div class="eb" style="left:25px">15 · Exit Strategy</div>
  <h2 class="t" style="left:25px">Creating Future <em>Exit Opportunities</em></h2>
  <div class="lead" style="left:25px;top:48px"><span style="position:static;display:inline-block;width:10px;border-top:1px solid var(--orange);vertical-align:middle;margin-right:4px"></span>A mature franchise system opens five distinct exit paths — each rewarding recurring royalty revenue at a premium.</div>
  <div class="flow" style="position:absolute;left:25px;top:64px;width:434px;display:grid;grid-template-columns:repeat(5,1fr);gap:5px;height:120px">
    <div class="flow card" style="text-align:center;padding:8px 5px"><div class="flow" style="margin:0 auto;width:12px;height:12px;border-radius:3px;background:var(--navy)"></div><div class="flow h" style="font-size:3.9px;margin-top:14px">Potential<br>Outcomes</div><div class="flow p" style="font-size:3.3px;margin-top:6px">PE firms acquire franchise platforms for recurring royalty streams. Mature systems command 10–15× EBITDA.</div></div>
    <div class="flow card" style="text-align:center;padding:8px 5px"><div class="flow" style="margin:0 auto;width:12px;height:12px;border-radius:3px;background:var(--navy)"></div><div class="flow h" style="font-size:3.9px;margin-top:14px">STRONG<br>SYSTEMS</div><div class="flow p" style="font-size:3.3px;margin-top:6px">Industry consolidators pay a premium for category-leading franchise systems with proven unit economics.</div></div>
    <div class="flow card" style="text-align:center;padding:8px 5px"><div class="flow" style="margin:0 auto;width:12px;height:12px;border-radius:3px;background:var(--navy)"></div><div class="flow h" style="font-size:3.9px;margin-top:14px">RECURRING<br>REVENUE</div><div class="flow p" style="font-size:3.3px;margin-top:6px">Sell a majority stake to a sponsor while retaining operational control and upside. Take chips off the table.</div></div>
    <div class="flow card" style="text-align:center;padding:8px 5px"><div class="flow" style="margin:0 auto;width:12px;height:12px;border-radius:3px;background:var(--navy)"></div><div class="flow h" style="font-size:3.9px;margin-top:14px">GREATER<br>VALUE</div><div class="flow p" style="font-size:3.3px;margin-top:6px">Transfer ownership to the next generation with a documented, recurring-revenue business in place.</div></div>
    <div class="flow card" style="text-align:center;padding:8px 5px"><div class="flow" style="margin:0 auto;width:12px;height:12px;border-radius:3px;background:var(--navy)"></div><div class="flow h" style="font-size:3.9px;margin-top:14px">BRIGHTER<br>FUTURE</div><div class="flow p" style="font-size:3.3px;margin-top:6px">Retain 100% ownership and let recurring royalty revenue fund lifestyle, philanthropy, and new ventures.</div></div>
  </div>
  <div class="bar" style="left:25px;top:200px;width:434px;height:30px">
    <div style="left:10px;top:9px;font:700 3.4px/1.4 'Montserrat';color:var(--orange);letter-spacing:.08em">THE<br>PRINCIPLE</div>
    <div style="left:58px;top:11px;font:italic 4.8px 'Open Sans'">Every franchise sold today may contribute to enterprise value tomorrow.</div>
  </div>
  <footer class="foot"><span>OUTPOST LATTICE ADVISORS</span><span>CONFIDENTIAL</span><span>15 / 19</span></footer>
</section>

<!-- 16 Why different -->
<section class="s" style="left:35px;top:847px">
  <div class="eb" style="left:24px">16 · Why OLA</div>
  <h2 class="t" style="left:24px;font-size:13px">Why Outpost Lattice <em>Advisors Is Different</em></h2>
  <div class="lead" style="left:24px;top:48px"><span style="position:static;display:inline-block;width:10px;border-top:1px solid var(--orange);vertical-align:middle;margin-right:4px"></span>Seven reasons founders, executives, and investors choose OLA as their fractional franchise development partner.</div>
  <div class="navy" style="left:24px;top:80px;width:145px;height:167px;border-radius:4px">
    <div style="left:12px;top:18px;font:700 3.8px 'Montserrat';letter-spacing:.1em;color:var(--orange)">SIGNATURE STAT</div>
    <div style="left:12px;top:30px;font:800 27px 'Montserrat';color:#fff">550+</div>
    <div style="left:12px;top:74px;width:18px;border-top:1.5px solid var(--orange)"></div>
    <div style="left:12px;top:82px;font:600 6.5px 'Montserrat';color:#fff">Franchise Sales Closed</div>
    <div style="left:12px;top:96px;width:110px;font-size:3.8px;line-height:1.5;color:#c3cbd8">Across 30+ years and multiple brand categories — a repeatable, proven franchise development motion.</div>
  </div>
  <div class="flow" style="position:absolute;left:176px;top:80px;width:274px;display:grid;grid-template-columns:repeat(3,1fr);grid-template-rows:1fr 1fr;gap:5px;height:167px">
    <div class="flow card" style="padding:7px"><span class="ring" style="position:relative;display:block"></span><div class="flow h" style="font-size:4.2px;margin-top:10px">Fractional Cost Model</div><div class="flow p" style="font-size:3.5px;margin-top:2px">Director-level output at sub-director cost. Pay for the capacity you need.</div></div>
    <div class="flow card" style="padding:7px"><span class="ring" style="position:relative;display:block"></span><div class="flow h" style="font-size:4.2px;margin-top:10px">Immediate Execution</div><div class="flow p" style="font-size:3.5px;margin-top:2px">No recruiting delay. Engagements launch within 2–3 weeks of signature.</div></div>
    <div class="flow card" style="padding:7px"><span class="ring" style="position:relative;display:block"></span><div class="flow h" style="font-size:4.2px;margin-top:10px">30+ Years Experience</div><div class="flow p" style="font-size:3.5px;margin-top:2px">Three decades of franchise sales leadership across every cycle.</div></div>
    <div class="flow card" style="padding:7px"><span class="ring" style="position:relative;display:block"></span><div class="flow h" style="font-size:4.2px;margin-top:10px">Established Broker Network</div><div class="flow p" style="font-size:3.5px;margin-top:2px">Active, trusted relationships with all six major franchise broker networks.</div></div>
    <div class="flow card" style="padding:7px"><span class="ring" style="position:relative;display:block"></span><div class="flow h" style="font-size:4.2px;margin-top:10px">Proven Growth Systems</div><div class="flow p" style="font-size:3.5px;margin-top:2px">Documented processes for every stage from lead to award.</div></div>
    <div class="flow card" style="padding:7px"><span class="ring" style="position:relative;display:block"></span><div class="flow h" style="font-size:4.2px;margin-top:10px">Strategic Growth Partner</div><div class="flow p" style="font-size:3.5px;margin-top:2px">Not a vendor — a long-term partner aligned to your enterprise value goals.</div></div>
  </div>
  <footer class="foot"><span>OUTPOST LATTICE ADVISORS</span><span>CONFIDENTIAL</span><span>16 / 19</span></footer>
</section>

<!-- 17 Engagement options -->
<section class="s" style="left:313px;top:847px">
  <div class="eb" style="left:24px">17 · How to Engage</div>
  <h2 class="t" style="left:24px">Engagement <em>Options</em></h2>
  <div class="lead" style="left:24px;top:48px"><span style="position:static;display:inline-block;width:10px;border-top:1px solid var(--orange);vertical-align:middle;margin-right:4px"></span>Five ways to work with OLA — sold as standalone engagements or combined into an integrated franchise development program.</div>
  <div class="flow" style="position:absolute;left:24px;top:62px;width:436px;display:flex;flex-direction:column;gap:6px">
    <div class="flow card" style="height:28px;display:grid;grid-template-columns:24px 90px 1fr 40px;align-items:center;padding:0 6px"><span class="ring" style="position:relative"></span><span class="flow h" style="font-size:4.2px">Franchise Sales Outsourcing</span><span class="flow p" style="font-size:3.7px;border-left:1px solid var(--orange);padding-left:6px">Full-cycle sales execution — we become your franchise development team.</span><span class="flow" style="font:600 3.8px 'Montserrat';color:var(--orange);text-align:right">Included</span></div>
    <div class="flow card" style="height:28px;display:grid;grid-template-columns:24px 90px 1fr 40px;align-items:center;padding:0 6px"><span class="ring" style="position:relative"></span><span class="flow h" style="font-size:4.2px">Broker Network Development</span><span class="flow p" style="font-size:3.7px;border-left:1px solid var(--orange);padding-left:6px">Activate and manage broker relationships across all six major networks.</span><span class="flow" style="font:600 3.8px 'Montserrat';color:var(--orange);text-align:right">Included</span></div>
    <div class="flow card" style="height:28px;display:grid;grid-template-columns:24px 90px 1fr 40px;align-items:center;padding:0 6px"><span class="ring" style="position:relative"></span><span class="flow h" style="font-size:4.2px">Franchise Growth Consulting</span><span class="flow p" style="font-size:3.7px;border-left:1px solid var(--orange);padding-left:6px">Strategic guidance on system design, unit economics, and growth cadence.</span><span class="flow" style="font:600 3.8px 'Montserrat';color:var(--orange);text-align:right">Included</span></div>
    <div class="flow card" style="height:28px;display:grid;grid-template-columns:24px 90px 1fr 40px;align-items:center;padding:0 6px"><span class="ring" style="position:relative"></span><span class="flow h" style="font-size:4.2px">Franchise Expansion Strategy</span><span class="flow p" style="font-size:3.7px;border-left:1px solid var(--orange);padding-left:6px">Market selection, launch sequencing, and franchisee profile definition.</span><span class="flow" style="font:600 3.8px 'Montserrat';color:var(--orange);text-align:right">Included</span></div>
    <div class="flow card" style="height:28px;display:grid;grid-template-columns:24px 90px 1fr 40px;align-items:center;padding:0 6px"><span class="ring" style="position:relative"></span><span class="flow h" style="font-size:4.2px">Franchise Development<br>Advisory Services</span><span class="flow p" style="font-size:3.7px;border-left:1px solid var(--orange);padding-left:6px">Fractional executive advisory for founders building an internal development function.</span><span class="flow" style="font:600 3.8px 'Montserrat';color:var(--orange);text-align:right">Included</span></div>
  </div>
  <footer class="foot"><span>OUTPOST LATTICE ADVISORS</span><span>CONFIDENTIAL</span><span>17 / 19</span></footer>
</section>

<!-- 18 Executive summary -->
<section class="s" style="left:591px;top:847px">
  <div class="eb">18 · Success Highlights</div>
  <h2 class="t">Executive <em>Summary</em></h2>
  <div class="flow" style="position:absolute;left:210px;top:42px;width:240px;display:flex;flex-direction:column;gap:6px">
    <div class="flow" style="height:34px;background:var(--pill);border-radius:4px;display:flex;align-items:center;gap:7px;padding:0 7px"><span class="ring" style="position:relative"></span><span class="h" style="font-size:5.2px">Fractional Franchise Sales - Reduce cost &amp; Risk</span></div>
    <div class="flow" style="height:34px;background:var(--pill);border-radius:4px;display:flex;align-items:center;gap:7px;padding:0 7px"><span class="ring" style="position:relative"></span><span class="h" style="font-size:5.2px">Instant Access to Franchise Broker Community</span></div>
    <div class="flow" style="height:34px;background:var(--pill);border-radius:4px;display:flex;align-items:center;gap:7px;padding:0 7px"><span class="ring" style="position:relative"></span><span class="h" style="font-size:5.2px">Experienced Franchise Sales</span></div>
    <div class="flow" style="height:34px;background:var(--pill);border-radius:4px;display:flex;align-items:center;gap:7px;padding:0 7px"><span class="ring" style="position:relative"></span><span class="h" style="font-size:5.2px">Proven Franchise Sales Process</span></div>
    <div class="flow" style="height:34px;background:var(--pill);border-radius:4px;display:flex;align-items:center;gap:7px;padding:0 7px"><span class="ring" style="position:relative"></span><span class="h" style="font-size:5.2px">Creating Future Exit &amp; Growth Opportunities</span></div>
  </div>
  <footer class="foot"><span>OUTPOST LATTICE ADVISORS</span><span>CONFIDENTIAL</span><span>18 / 19</span></footer>
</section>

<!-- 19 Closing -->
<section class="s" style="left:35px;top:1014px;background:var(--navy)">
  <div class="eb" style="left:0;right:0;top:24px;text-align:center">Next Step</div>
  <div style="left:0;right:0;top:34px;text-align:center;font:700 13px/1.45 'Montserrat';color:#fff">Let's Build<br>Your <span style="position:static;color:var(--orange)">Growth Plan.</span></div>
  <div style="left:120px;right:120px;top:80px;text-align:center;font-size:4.6px;line-height:1.6;color:#c9d1de">Schedule a Franchise Growth Strategy Consultation. We will review your current pipeline, broker exposure, and unit economics — and map the fastest path to your next 20, 50, or 100 franchise units.</div>
  <div style="left:232px;top:116px;width:7px;height:7px;border-radius:50%;border:1px solid #fff"></div>
  <div style="left:245px;top:116px;width:7px;height:7px;border-radius:50%;border:1px solid #fff"></div>
  <div style="left:0;right:0;top:128px;text-align:center;font-size:4.2px;color:#fff">www.outpostlatticeadvisors.example &nbsp;|&nbsp; info@outpostlatticeadvisors.example</div>
  <div style="left:201px;top:143px;width:82px;height:14px;border-radius:4px;background:var(--orange);text-align:center;font:700 4.4px/14px 'Montserrat';color:var(--navy)">Schedule a Consultation →</div>
  <div style="left:27px;top:242px;font-size:4px;color:#fff">Follow Us On :</div>
  <div style="left:62px;top:241px;width:6px;height:6px;border-radius:50%;background:var(--orange)"></div>
  <div style="left:70px;top:241px;width:6px;height:6px;border-radius:50%;background:var(--orange)"></div>
  <div style="right:14px;top:257px;font:600 4px 'Montserrat';letter-spacing:.12em;color:#8796ad">CONFIDENTIAL · 2026</div>
</section>

</body>
</html>
```